Calderwood Membership Company need a book cover designing. The book is called "Harvest T...

Please submit it as a jpg at 300 dpi with A5 dimensions (14.8 cm wide by 21 cm high), and make sure that your text is well within the trim line - approximately 2 cm from the edge. We like the style "Harvest" is written in the attached image, although this is a guideline. It CANNOT be copied, but it may provide influence and inspiration. We are looking for a crisp and clean book cover, so probably on a white background.Our Logo is also attached and we see this being included centered at the bottom "There is a better way to grow your savings" is what the book is about

```html
<!DOCTYPE html>
<html lang="en">
<head>
<meta charset="utf-8">
<title>Harvest Tom – Book Cover</title>
<link href="https://fonts.googleapis.com/css2?family=Dancing+Script:wght@500;600&family=Montserrat:wght@300;600&display=swap" rel="stylesheet">
<style>
  :root {
    --backdrop: #ecebe8;
    --cover-white: #ffffff;
    --ink: #2b2b2b;
    --ink-soft: #3a3a3a;
    --photo-top: #ffffff;
    --photo-haze: #f7f2ef;
    --photo-coins-light: #eadbd1;
    --photo-coins: #d8bca9;
    --photo-table: #cfa68f;
    --photo-table-deep: #c29279;
    --logo-ink: #ffffff;
  }
  * { margin: 0; padding: 0; box-sizing: border-box; }
  html, body {
    width: 1200px;
    height: 1200px;
    overflow: hidden;
    background: var(--backdrop);
  }
  .book-cover {
    position: absolute;
    left: 198px;
    top: 30px;
    width: 804px;
    height: 1140px;
    background: var(--cover-white);
    box-shadow: 0 6px 24px rgba(0,0,0,0.12);
    overflow: hidden;
  }
  .cover-title {
    position: absolute;
    left: 0;
    right: 0;
    top: 105px;
    text-align: center;
    font-family: "Dancing Script", cursive;
    font-weight: 600;
    color: var(--ink);
    line-height: 1;
  }
  .cover-title .title-line { display: block; }
  .cover-title .title-first { font-size: 176px; }
  .cover-title .title-second { font-size: 168px; margin-top: 22px; }
  .cover-tagline {
    position: absolute;
    left: 0;
    right: 0;
    top: 558px;
    text-align: center;
    font-family: "Montserrat", sans-serif;
    color: var(--ink-soft);
    line-height: 1.3;
  }
  .tagline-lead {
    display: block;
    font-weight: 300;
    font-size: 24px;
    letter-spacing: 2.5px;
  }
  .tagline-emphasis {
    display: block;
    font-weight: 600;
    font-size: 24px;
    letter-spacing: 3px;
  }
  .cover-photo {
    position: absolute;
    left: 0;
    right: 0;
    top: 650px;
    bottom: 0;
    background: linear-gradient(to bottom,
      var(--photo-top) 0%,
      var(--photo-haze) 28%,
      var(--photo-coins-light) 45%,
      var(--photo-coins) 72%,
      var(--photo-table) 76%,
      var(--photo-table-deep) 100%);
  }
  .publisher-mark {
    position: absolute;
    left: 0;
    right: 0;
    bottom: 46px;
    display: flex;
    justify-content: center;
    align-items: center;
    gap: 12px;
    font-family: "Montserrat", sans-serif;
    font-weight: 600;
    font-size: 24px;
    letter-spacing: 3px;
    color: var(--logo-ink);
  }
  .publisher-dot {
    width: 36px;
    height: 36px;
    border-radius: 50%;
    background: var(--logo-ink);
  }
</style>
</head>
<body>
  <main class="book-cover">
    <h1 class="cover-title">
      <span class="title-line title-first">Harvest</span>
      <span class="title-line title-second">Tom</span>
    </h1>
    <p class="cover-tagline">
      <span class="tagline-lead">THERE IS A BETTER WAY TO</span>
      <span class="tagline-emphasis">GROW YOUR SAVINGS</span>
    </p>
    <div class="cover-photo" role="img" aria-label="Photo of three rising stacks of coins on a table with green seedlings sprouting from their tops"></div>
    <div class="publisher-mark">
      <span class="publisher-dot"></span>
      <span class="publisher-name">HARVEST TOM</span>
    </div>
  </main>
</body>
</html>
```